Business Card Design

Need business card design for all carpentry & construction solutions. We would like to see designs that use black as a background with orange writing as it would stand out.

Business

RVK CONTRACTING
MARTIN COLLIER
14 KESTWICK ST
MARLOWE HILLS
WA 6614
0487315962
rvkcontracting@mailvesta.com

```html
<!DOCTYPE html>
<html lang="en">
<head>
<meta charset="utf-8">
<title>RVK Contracting – Business Card</title>
<link href="https://fonts.googleapis.com/css2?family=Questrial&family=Montserrat:wght@500;600&display=swap" rel="stylesheet">
<style>
  :root {
    --backdrop: #e4e4e6;
    --card-black: #050505;
    --brand-orange: #f05a24;
    --brand-orange-light: #f26b23;
    --brand-orange-deep: #ea4d20;
    --ink-white: #ffffff;
  }
  * { margin: 0; padding: 0; box-sizing: border-box; }
  html, body { width: 1200px; height: 800px; overflow: hidden; }
  body {
    background: var(--backdrop);
    position: relative;
    font-family: "Montserrat", sans-serif;
  }
  .card {
    position: absolute;
    width: 560px;
    height: 340px;
    overflow: hidden;
    box-shadow: 0 8px 22px rgba(0,0,0,0.18);
  }
  .card svg.card-lines { position: absolute; inset: 0; }

  /* Front */
  .card-front { left: 60px; top: 60px; background: var(--card-black); }
  .front-name {
    position: absolute;
    left: 60px; top: 88px;
    width: 380px;
    text-align: center;
    font-family: "Questrial", sans-serif;
    color: var(--brand-orange);
    line-height: 1;
  }
  .front-name .name-main { display: block; font-size: 96px; letter-spacing: 6px; }
  .front-name .name-sub { display: block; font-size: 33px; letter-spacing: 4px; margin-top: 8px; }

  /* Back */
  .card-back { left: 580px; top: 420px; background: var(--card-black); }
  .back-name {
    position: absolute;
    left: 210px; top: 62px;
    width: 240px;
    text-align: center;
    font-family: "Questrial", sans-serif;
    color: var(--ink-white);
    line-height: 1;
  }
  .back-name .name-main { display: block; font-size: 62px; letter-spacing: 4px; }
  .back-name .name-sub { display: block; font-size: 21px; letter-spacing: 2.5px; margin-top: 6px; }

  .contact {
    position: absolute;
    left: 34px; top: 152px;
    color: var(--ink-white);
  }
  .contact-person { font-weight: 600; font-size: 19px; letter-spacing: 0.5px; }
  .contact-role { font-size: 13px; font-weight: 500; margin: 2px 0 0 12px; }
  .contact-list { list-style: none; margin-top: 14px; }
  .contact-list li {
    display: flex; align-items: flex-start; gap: 8px;
    font-size: 13px; font-weight: 500; line-height: 1.3;
    margin-bottom: 6px;
  }
  .contact-list svg { flex: none; width: 18px; height: 18px; margin-top: 1px; }
  .contact-phone { font-size: 15px; letter-spacing: 1px; }
  .contact-email { font-size: 12px; }
  .contact-address { text-transform: uppercase; letter-spacing: 0.5px; }
</style>
</head>
<body>

  <section class="card card-front" aria-label="Business card front">
    <svg class="card-lines" width="560" height="340" viewBox="0 0 560 340" aria-hidden="true">
      <path d="M0 292 H438 Q460 292 460 270 V48 Q460 0 490 0"
            fill="none" stroke="var(--brand-orange)" stroke-width="3"/>
    </svg>
    <div class="front-name">
      <span class="name-main">RVK</span>
      <span class="name-sub">CONTRACTING</span>
    </div>
  </section>

  <section class="card card-back" aria-label="Business card back">
    <svg class="card-lines" width="560" height="340" viewBox="0 0 560 340" aria-hidden="true">
      <defs>
        <linearGradient id="orangeFace" x1="0" y1="0" x2="1" y2="0">
          <stop offset="0" stop-color="var(--brand-orange-deep)"/>
          <stop offset="0.65" stop-color="var(--brand-orange-light)"/>
          <stop offset="1" stop-color="var(--brand-orange-deep)"/>
        </linearGradient>
      </defs>
      <path d="M0 6 H420 Q470 6 470 56 V120 Q470 140 492 140 H560 V340 H0 Z"
            fill="url(#orangeFace)"/>
      <path d="M0 6 H420 Q470 6 470 56 V120 Q470 140 492 140 H560"
            fill="none" stroke="var(--ink-white)" stroke-width="4"/>
    </svg>

    <div class="back-name">
      <span class="name-main">RVK</span>
      <span class="name-sub">CONTRACTING</span>
    </div>

    <div class="contact">
      <p class="contact-person">MARTIN COLLIER</p>
      <p class="contact-role">Owner</p>
      <ul class="contact-list">
        <li>
          <svg viewBox="0 0 24 24" aria-hidden="true"><path d="M3 10c0-4 4-6 9-6s9 2 9 6l-4 1-1-3H8L7 11z M7 13h10l2 7H5z" fill="none" stroke="#fff" stroke-width="1.8" stroke-linejoin="round"/></svg>
          <span class="contact-phone">048 731 5962</span>
        </li>
        <li>
          <svg viewBox="0 0 24 24" aria-hidden="true"><rect x="2.5" y="5" width="19" height="14" fill="none" stroke="#fff" stroke-width="1.8"/><path d="M2.5 5l9.5 8 9.5-8M2.5 19l7-7M21.5 19l-7-7" fill="none" stroke="#fff" stroke-width="1.6"/></svg>
          <span class="contact-email">rvkcontracting@mailvesta.com</span>
        </li>
        <li>
          <svg viewBox="0 0 24 24" aria-hidden="true"><path d="M12 2a7 7 0 0 0-7 7c0 5 7 13 7 13s7-8 7-13a7 7 0 0 0-7-7z" fill="#fff"/><circle cx="12" cy="9" r="2.6" fill="var(--brand-orange)"/></svg>
          <span class="contact-address">14 Kestwick St<br>Marlowe Hills<br>WA 6614</span>
        </li>
      </ul>
    </div>
  </section>

</body>
</html>
```